Business Card for Beach theme sports bar called TAVRU

I need a business card designed for our employees, front and back. This will be used by the employees of two business locations to hand out to customers. I've attached the previous business cards we used at one time for a Benwicks (it is now Tavru). Looking for a fresh new card that is elegant but has character.

Target Market(s)

30-60, middle class

Contact Information for Business Card

We are a beach bar and sports bar. I am looking for an elegant business card with the front to have the TAVRU logo. Then on the back I need it to allow a space for employees to write their names and for them to write in their schedule. I have attached our old cards with our old name Benwicks so you can pull everything we need on the cards. one thing is missing is we have another location at 2815 N Willow Crest Rd with a number of 702-418-9351. Since we will use it for both locations it should allow the employee to circle or check mark the bar which they work at.

Font styles to use
Sans Serif

Requirements
Must have
• We are looking for some fresh ideas for the business card. Something that will really stick out to customers when the staff hands them out. Creativity will be looked at positively, but we still want it to look upscale and fun.

```html
<!DOCTYPE html>
<html lang="en">
<head>
<meta charset="utf-8">
<title>Tavru – Business Card</title>
<link href="https://fonts.googleapis.com/css2?family=Arimo:wght@700&family=Tinos:ital@0;1&display=swap" rel="stylesheet">
<style>
  :root {
    --page-bg: #d9d9d9;
    --card-dark: #231f20;
    --card-light: #f4f5f3;
    --ink-white: #ffffff;
    --ink-gray: #8a8a8a;
    --ink-soft: #e6e7e5;
    --accent-yellow: #ffcc00;
    --line-gray: #8f8f8f;
  }
  * { margin: 0; padding: 0; box-sizing: border-box; }
  html, body { width: 1200px; height: 1200px; overflow: hidden; background: var(--page-bg); }
  .canvas { position: relative; width: 1200px; height: 1200px; }
  .card { position: absolute; left: 250px; width: 708px; height: 404px; overflow: hidden; }
  .card-front { top: 144px; background: var(--card-dark); }
  .card-back { top: 582px; background: var(--card-light); }

  .brand-name {
    position: absolute; left: 0; right: 0; top: 110px; text-align: center;
    font-family: "Tinos", serif; font-size: 120px; line-height: 1; color: var(--ink-white);
  }
  .tagline {
    position: absolute; left: 0; right: 0; top: 318px; text-align: center;
    font-family: "Tinos", serif; font-size: 34px; color: var(--ink-white); letter-spacing: 0.5px;
  }

  .offer {
    position: absolute; left: 0; right: 0; top: 24px; text-align: center;
    font-family: "Arimo", sans-serif; font-weight: 700; font-size: 76px; line-height: 1;
    color: var(--accent-yellow); letter-spacing: -0.5px;
  }
  .brand-watermark {
    position: absolute; left: 30px; top: 228px;
    font-family: "Tinos", serif; font-size: 140px; line-height: 1; color: var(--ink-soft);
  }
  .label-bartender {
    position: absolute; left: 38px; top: 116px;
    font-family: "Arimo", sans-serif; font-weight: 700; font-size: 36px; color: var(--ink-gray);
  }
  .name-box {
    position: absolute; left: 40px; top: 166px; width: 222px; height: 56px;
    border: 2px solid var(--line-gray);
  }
  .schedule { position: absolute; left: 312px; top: 138px; display: flex; }
  .day { width: 50.5px; text-align: center; }
  .day-label {
    font-family: "Arimo", sans-serif; font-weight: 700; font-size: 24px; color: var(--ink-gray);
    height: 36px; line-height: 30px;
  }
  .day-box { width: 50.5px; height: 41px; border: 2px solid var(--line-gray); margin-left: -1px; }

  .location {
    position: absolute; text-align: center;
    font-family: "Tinos", serif; font-size: 21px; line-height: 27px; color: var(--ink-gray);
  }
  .location-north { left: 60px; width: 240px; top: 270px; }
  .location-west { left: 430px; width: 212px; top: 256px; }
  .fine-print {
    position: absolute; left: 0; right: 0; top: 368px; text-align: center;
    font-family: "Tinos", serif; font-style: italic; font-size: 11.5px; color: var(--ink-gray);
  }
</style>
</head>
<body>
<main class="canvas">
  <section class="card card-front">
    <div class="brand-name">Tavru</div>
    <div class="tagline">A Gamers Bar</div>
  </section>

  <section class="card card-back">
    <div class="brand-watermark" aria-hidden="true">Tavru</div>
    <div class="offer">$20 MATCH PLAY</div>
    <div class="label-bartender">Bartender</div>
    <div class="name-box"></div>
    <div class="schedule">
      <div class="day"><div class="day-label">M</div><div class="day-box"></div></div>
      <div class="day"><div class="day-label">T</div><div class="day-box"></div></div>
      <div class="day"><div class="day-label">W</div><div class="day-box"></div></div>
      <div class="day"><div class="day-label">Th</div><div class="day-box"></div></div>
      <div class="day"><div class="day-label">F</div><div class="day-box"></div></div>
      <div class="day"><div class="day-label">Sa</div><div class="day-box"></div></div>
      <div class="day"><div class="day-label">Su</div><div class="day-box"></div></div>
    </div>
    <address class="location location-north">2815 N Willow Crest Rd<br>702-418-9351</address>
    <address class="location location-west">3360 W Harbor Palm Rd<br>Las Vegas, NV 89146<br>702-563-2184<br>cs@tavrubar.com</address>
    <p class="fine-print">Match play for new slot members, must play total 100 coin. &nbsp;Please see bartender for details. &nbsp;Management reserves all rights</p>
  </section>
</main>
</body>
</html>
```